Artist business cards needed, happy acrylic painter

I'd like a business card I can hand out to people interested in my paintings. I'd like a logo that includes elements of my painting. I have shared a collection that may be used at https://qlvbox.example/albums/7TrpWdKz3mNa8bQeXy
I get my vibe and the type of art I create, you can also see my active Vornet Circle account: https://circle.vornetso.example/+MirelaQuade

Target Market(s)

people interested in art

Industry/Entity Type

Artists

Contact Information for Business Card

Mirela Quade
555-014-7392
mirelaquade@postvale.example
mirelaquade@postvale.example
www.mirelaquade.example

Font styles to use
Sans Serif
Decorative
Script

Requirements
Must have
• 1. Colors that are represented in my paintings
• 2. Elements from my paintings: Link to the vornet locker with my art: https://qlvbox.example/albums/7TrpWdKz3mNa8bQeXy
• 3. Flower(s)
• 4. A box on the back that's outlined so a note could be added. I've attached a photo of a business card my friend uses for her floral design company as an example of the back of the card with the quote and a box and business name (Mirela Quade).
• 4. I'd like to have this quote on the back of the card too.
• "I must have flowers, always and always."
• ~Tobiah Varnsell
Nice to have
• In smaller font
• If it fits, links to my other social media:
• https://circle.vornetso.example/+MirelaQuade
• https://www.friendlane.example/mirelaquadeartist/
Should not have
• A dark background

```html
<!DOCTYPE html>
<html lang="en">
<head>
<meta charset="utf-8">
<title>Mirela Quade — Business Card</title>
<link href="https://fonts.googleapis.com/css2?family=Questrial&display=swap" rel="stylesheet">
<style>
  :root {
    --page: #efece6;
    --card: #ffffff;
    --ink: #4a4a4a;
    --name: #8a4fa3;
    --frame: #e0819d;
    --quote: #9a86b8;
    --mark: #f0b63c;
    --paint-sky: #bcd9ec;
    --paint-green: #7fbf5a;
    --paint-pink: #e586a8;
    --paint-violet: #9b79c9;
    --paint-orange: #f2a04a;
  }
  * { box-sizing: border-box; margin: 0; padding: 0; }
  html, body { width: 725px; height: 1200px; overflow: hidden; }
  body {
    background: var(--page);
    font-family: "Questrial", "Century Gothic", sans-serif;
    color: var(--ink);
    position: relative;
  }
  .card {
    position: absolute;
    left: 207px;
    width: 310px;
    height: 542px;
    background: var(--card);
    box-shadow: 0 2px 10px rgba(0,0,0,0.12);
    overflow: hidden;
  }
  .card--front { top: 29px; }
  .card--back { top: 629px; }

  .brand { display: flex; align-items: center; gap: 8px; }
  .brand__square { width: 26px; height: 26px; background: var(--mark); }
  .brand__name { font-size: 24px; color: var(--name); letter-spacing: 0.5px; }

  .card--front .brand { position: absolute; top: 40px; left: 30px; }

  .contact { position: absolute; top: 96px; left: 30px; right: 16px; list-style: none; }
  .contact__item {
    display: flex; align-items: center; gap: 9px;
    font-size: 12.5px; line-height: 1.2; margin-bottom: 9px; word-break: break-all;
  }
  .contact__icon { flex: 0 0 14px; width: 14px; height: 14px; }
  .contact__item--small { font-size: 10.5px; }

  .painting { position: absolute; left: 0; bottom: 0; width: 310px; height: 330px; }

  .quote {
    position: absolute; top: 26px; left: 24px; right: 22px;
    text-align: right; color: var(--quote); font-size: 15px; line-height: 1.3;
  }
  .quote__by { display: block; margin-top: 2px; }

  .note {
    position: absolute; top: 108px; left: 24px; width: 262px; height: 290px;
    border: 2px solid var(--frame);
  }
  .note__label {
    position: absolute; top: 94px; left: 24px;
    font-size: 14px; color: var(--ink); transform: translateY(-100%);
  }
  .card--back .brand { position: absolute; bottom: 40px; left: 24px; }
  .card--back .brand__name { font-size: 20px; }
</style>
</head>
<body>

<section class="card card--front" aria-label="Card front">
  <div class="brand">
    <span class="brand__square"></span>
    <span class="brand__name">Mirela Quade</span>
  </div>

  <ul class="contact">
    <li class="contact__item">
      <svg class="contact__icon" viewBox="0 0 14 14"><path d="M3 1h2l1 3-1.5 1a7 7 0 0 0 4 4L10 7.5l3 1v2c0 1-1 2-2 2A10 10 0 0 1 1 3c0-1 1-2 2-2z" fill="var(--name)"/></svg>
      555-014-7392
    </li>
    <li class="contact__item">
      <svg class="contact__icon" viewBox="0 0 14 14"><rect x="1" y="3" width="12" height="8" fill="var(--paint-violet)"/><path d="M1 3l6 5 6-5" fill="none" stroke="#fff" stroke-width="1.2"/></svg>
      mirelaquade@postvale.example
    </li>
    <li class="contact__item">
      <svg class="contact__icon" viewBox="0 0 14 14"><circle cx="7" cy="7" r="5.5" fill="none" stroke="var(--mark)" stroke-width="1.3"/><path d="M1.5 7h11M7 1.5c-3 3-3 8 0 11M7 1.5c3 3 3 8 0 11" fill="none" stroke="var(--mark)" stroke-width="1"/></svg>
      www.mirelaquade.example
    </li>
    <li class="contact__item contact__item--small">
      <svg class="contact__icon" viewBox="0 0 14 14"><rect x="1" y="1" width="12" height="12" fill="var(--paint-pink)"/></svg>
      circle.vornetso.example/+MirelaQuade
    </li>
    <li class="contact__item contact__item--small">
      <svg class="contact__icon" viewBox="0 0 14 14"><rect x="1" y="1" width="12" height="12" fill="var(--paint-violet)"/></svg>
      friendlane.example/mirelaquadeartist/
    </li>
  </ul>

  <svg class="painting" viewBox="0 0 310 330" role="img" aria-label="Acrylic painting of a colourful flower garden with a tree under a pale blue sky">
    <defs>
      <linearGradient id="gardenTone" x1="0" y1="0" x2="1" y2="1">
        <stop offset="0" stop-color="var(--paint-sky)"/>
        <stop offset="0.3" stop-color="var(--paint-orange)"/>
        <stop offset="0.55" stop-color="var(--paint-pink)"/>
        <stop offset="0.8" stop-color="var(--paint-violet)"/>
        <stop offset="1" stop-color="var(--paint-green)"/>
      </linearGradient>
    </defs>
    <path d="M0 40 C80 70 140 120 210 150 C250 167 285 170 310 168 V330 H0 Z" fill="url(#gardenTone)"/>
  </svg>
</section>

<section class="card card--back" aria-label="Card back">
  <p class="quote">“I must have flowers, always and always.”
    <span class="quote__by">~Tobiah Varnsell</span>
  </p>
  <span class="note__label">Note:</span>
  <div class="note"></div>
  <div class="brand">
    <span class="brand__square"></span>
    <span class="brand__name">Mirela Quade</span>
  </div>
</section>

</body>
</html>
```